Harborline I.T.
Harborline I.T. -
Creative Brief
Modern
Daniel Whitcombe
Owner
1875 Crandall Brook Ct. Larkmoor, OR 97415
dwhitcombe@harbolintech.example
Can use either business name on cards (Harborline I.T. --- or --- Harborline Information Technologies) whichever works best for you.

```html
<!DOCTYPE html>
<html lang="en">
<head>
<meta charset="utf-8">
<title>Harborline I.T. – Stationery</title>
<link href="https://fonts.googleapis.com/css2?family=Arimo:wght@400;700&display=swap" rel="stylesheet">
<style>
  :root{
    --backdrop:#3b3b3d;
    --paper:#ffffff;
    --ink:#222222;
    --ink-soft:#555555;
    --brand-blue:#1f6fc4;
    --brand-blue-light:#4a9be6;
    --brand-dark:#111111;
  }
  *{box-sizing:border-box;margin:0;padding:0}
  html,body{width:1200px;height:686px;overflow:hidden}
  body{background:var(--backdrop);font-family:'Arimo',Arial,sans-serif;color:var(--ink);position:relative}
  .sheet{position:absolute;background:var(--paper);overflow:hidden;box-shadow:0 2px 6px rgba(0,0,0,.35)}

  /* plain footer bands: thin dark rule above a flat blue band */
  .footer-band{position:absolute;left:0;bottom:0;width:100%;background:var(--brand-blue)}
  .footer-rule{position:absolute;left:0;width:100%;background:var(--brand-dark)}

  .brand{display:flex;align-items:center;gap:5px;color:var(--brand-blue);font-weight:700;letter-spacing:.04em;white-space:nowrap}
  .brand-dot{border-radius:50%;background:var(--brand-blue);flex:none}

  /* business cards */
  .card-front{left:30px;top:240px;width:218px;height:104px;border-radius:4px}
  .card-front .brand{position:absolute;left:12px;top:14px;font-size:9px}
  .card-front .brand-dot{width:10px;height:10px}
  .card-details{position:absolute;left:100px;top:30px;font-size:5px;line-height:1.45;color:var(--ink-soft)}
  .card-details .person{font-size:6.5px;font-weight:700;color:var(--ink)}
  .card-front .footer-band{height:10px}
  .card-front .footer-rule{bottom:13px;height:2px}

  .card-back{left:30px;top:360px;width:218px;height:104px;border-radius:4px}
  .card-back .brand{position:absolute;left:0;right:0;top:38px;justify-content:center;font-size:12px}
  .card-back .brand-dot{width:13px;height:13px}
  .card-back .footer-band{height:10px}
  .card-back .footer-rule{bottom:13px;height:2px}

  /* letterhead */
  .letterhead{left:257px;top:100px;width:384px;height:490px}
  .letterhead .brand{position:absolute;left:24px;top:52px;font-size:14px}
  .letterhead .brand-dot{width:16px;height:16px}
  .letterhead-contact{position:absolute;left:200px;top:20px;font-size:6px;line-height:1.5;color:var(--ink-soft)}
  .letterhead .footer-band{height:30px}
  .letterhead .footer-rule{bottom:36px;height:5px}

  /* envelope backs */
  .envelope-stack{position:absolute;left:660px;top:100px;width:330px;height:310px}
  .envelope-back{position:absolute;left:0;width:330px;height:150px}
  .envelope-back .brand{position:absolute;left:0;right:0;justify-content:center;font-size:9px}
  .envelope-back .brand-dot{width:10px;height:10px}
  .flap-white .brand{top:38px}
  .flap-dark .brand{top:30px;color:var(--paper)}
  .flap-dark .brand-dot{background:var(--paper)}
  .flap-blue .brand{top:30px;color:var(--paper)}
  .flap-blue .brand-dot{background:var(--paper)}

  /* envelope front */
  .envelope-front{left:660px;top:427px;width:330px;height:162px}
  .envelope-front .brand{position:absolute;left:14px;top:18px;font-size:10px}
  .envelope-front .brand-dot{width:11px;height:11px}
  .envelope-address{position:absolute;left:14px;top:40px;font-size:5px;line-height:1.5;color:var(--ink-soft)}
  .envelope-front .footer-band{height:14px}
  .envelope-front .footer-rule{bottom:18px;height:3px}
</style>
</head>
<body>

<section class="sheet card-front" aria-label="Business card front">
  <div class="brand"><span class="brand-dot"></span>HARBORLINE I.T.</div>
  <div class="card-details">
    <p class="person">Daniel Whitcombe</p>
    <p>Owner</p>
    <p>1875 Crandall Brook Ct. Larkmoor, OR 97415</p>
    <p>dwhitcombe@harbolintech.example</p>
  </div>
  <div class="footer-rule"></div>
  <div class="footer-band"></div>
</section>

<section class="sheet card-back" aria-label="Business card back">
  <div class="brand"><span class="brand-dot"></span>HARBORLINE I.T.</div>
  <div class="footer-rule"></div>
  <div class="footer-band"></div>
</section>

<section class="sheet letterhead" aria-label="Letterhead">
  <div class="brand"><span class="brand-dot"></span>HARBORLINE I.T.</div>
  <div class="letterhead-contact">
    <p>1875 Crandall Brook Ct.</p>
    <p>Larkmoor, OR 97415</p>
    <p>Phone: 541.555.0142</p>
    <p>Fax: 541.555.0143</p>
    <p>Email: dwhitcombe@harbolintech.example</p>
  </div>
  <div class="footer-rule"></div>
  <div class="footer-band"></div>
</section>

<div class="envelope-stack">
  <div class="envelope-back flap-white" style="top:0">
    <svg width="330" height="150" viewBox="0 0 330 150" aria-hidden="true">
      <rect width="330" height="150" fill="var(--paper)"/>
      <path d="M0 0 L330 0 L190 62 Q165 70 140 62Z" fill="var(--paper)" stroke="#cfcfcf"/>
    </svg>
    <div class="brand"><span class="brand-dot"></span>HARBORLINE I.T.</div>
  </div>
  <div class="envelope-back flap-dark" style="top:72px">
    <svg width="330" height="150" viewBox="0 0 330 150" aria-hidden="true">
      <path d="M0 0 L330 0 L190 62 Q165 70 140 62Z" fill="var(--brand-dark)"/>
    </svg>
    <div class="brand"><span class="brand-dot"></span>HARBORLINE I.T.</div>
  </div>
  <div class="envelope-back flap-blue" style="top:140px;height:170px">
    <svg width="330" height="170" viewBox="0 0 330 170" aria-hidden="true">
      <rect width="330" height="170" fill="var(--paper)"/>
      <path d="M0 0 L330 0 L190 62 Q165 70 140 62Z" fill="var(--brand-blue)"/>
    </svg>
    <div class="brand"><span class="brand-dot"></span>HARBORLINE I.T.</div>
  </div>
</div>

<section class="sheet envelope-front" aria-label="Envelope front">
  <div class="brand"><span class="brand-dot"></span>HARBORLINE I.T.</div>
  <div class="envelope-address">
    <p>1875 Crandall Brook Ct.</p>
    <p>Larkmoor, OR 97415</p>
  </div>
  <div class="footer-rule"></div>
  <div class="footer-band"></div>
</section>

</body>
</html>
```